Werbebanner-Design für klassischen Handwerksbetrieb
Zielgruppe
Wir sind ein klassischer Handwerksbetrieb Heizung/Sanitär.
und benötigen im Moment ein Design für ein hochwertiges ansprechendes Werbebanner am Parkplatz eines Fitnesstudios mit anspruchsvollem Publikum.
Dabei steht das Thema Badsanierung /Neubau im Vordergrund.
Wir begrüßen eine Offenheit für weitere Projekte
Aufgabenstellung
wenn ich hier einige Plakate liefere, mit denen wir uns aktuell präsentieren sollen diese für einen Einblick in das, was uns gefällt erleichtern. Wir freuen wir uns sehr über neue Ideen, Bilder und Gestaltungsvorschläge und deshalb stellen wir das Projekt hier sehr gern ein.
Dabei sollten ggf. diese Elemente vorkommen:
* eine Wasserwelle (denn die befindet sich auf allen unseren Firmenfahrzeugen)
* der große Wasserhahn (=unser Firmenlogo)
* Schriftzug 'Team Kupferbogen'Bernd Kowalke GmbH - mit dem wir ab April2019 in die Außenwirkung gehen
* 'Ein schönes Bad ist kein Zufall' als Markenschriftzug, wie geliefert
* die Maße sind in diesem Fall vorgegeben - 2,60m breit , 1,0 m hoch , darüber hinaus möchten wir es in 3 mind. weiteren Maßen benutzen können (Hoch- und Querformate)
Die Lieferung des LindWerk Bildmaterials kann bei Bedarf auch gern höher auflösend geliefert werden

```html
<!DOCTYPE html>
<html lang="de">
<head>
<meta charset="utf-8">
<title>Werbebanner Team Kupferbogen – Entwurf 1</title>
<link rel="stylesheet" href="https://fonts.googleapis.com/css2?family=Cabin:wght@400;500;600&family=Arimo:wght@400;700&display=swap">
<style>
  :root {
    --page: #ffffff;
    --navy: #2b2d6b;
    --pale-blue: #a3b5da;
    --pale-bar: #abbbdf;
    --bright-blue: #1f8fd1;
    --water-light: #dce6f2;
    --water-mid: #7e9cc4;
    --water-deep: #2f5d93;
    --frame: #c9c9c9;
    --rule: #9a9a9a;
    --text-dark: #1a1a1a;
  }
  * { box-sizing: border-box; margin: 0; padding: 0; }
  html, body { width: 812px; height: 1200px; overflow: hidden; background: var(--page); }
  body { position: relative; font-family: "Cabin", "Gill Sans", sans-serif; }

  .banner {
    position: absolute; left: 91px; width: 625px; height: 241px;
    background: var(--page); border: 1px solid var(--frame);
    box-shadow: 2px 2px 3px rgba(0,0,0,0.18); overflow: hidden;
  }
  .banner--navy { top: 159px; }
  .banner--pale { top: 452px; }
  .banner--bright { top: 743px; }

  .banner__water { position: absolute; left: 0; top: 0; width: 625px; height: 241px; }

  .brand-mark {
    position: absolute; left: 14px; top: 22px; width: 110px; height: 96px;
    display: flex; flex-direction: column; align-items: center; justify-content: center; gap: 6px;
  }
  .brand-mark__dot { width: 46px; height: 46px; border-radius: 50%; background: var(--navy); opacity: 0.85; }
  .brand-mark__name { font-size: 12px; font-weight: 600; color: var(--navy); }

  .headline {
    position: absolute; left: 143px; top: 38px; width: 265px;
    font-weight: 500; font-size: 33px; line-height: 34px; color: var(--pale-blue);
  }
  .banner--pale .headline, .banner--bright .headline { font-weight: 600; font-size: 31px; }
  .banner--bright .headline { color: var(--bright-blue); }
  .headline__line { display: block; }
  .headline__line--second { padding-left: 28px; }

  .tagline {
    position: absolute; right: 296px; top: 132px; text-align: right;
    color: var(--navy); font-size: 13.5px; line-height: 15px;
  }
  .banner--bright .tagline { right: 288px; }
  .tagline__company { display: block; font-weight: 400; color: var(--navy); opacity: 0.9; }

  .info-bar {
    position: absolute; left: 27px; top: 206px; width: 334px; height: 13px;
    display: flex; align-items: center; gap: 17px; padding-left: 12px;
    font-size: 7.5px; color: #fff;
  }
  .info-bar__company { font-size: 10px; font-weight: 600; }
  .banner--navy .info-bar { background: var(--navy); }
  .banner--pale .info-bar { background: var(--pale-bar); color: var(--navy); }
  .banner--bright .info-bar { background: var(--bright-blue); }

  .web-bar {
    position: absolute; left: 469px; top: 206px; width: 141px; height: 13px;
    display: flex; align-items: center; justify-content: flex-end; gap: 4px; padding-right: 10px;
    font-size: 8.5px; font-weight: 600;
  }
  .banner--navy .web-bar { background: var(--navy); color: #fff; }
  .banner--pale .web-bar { background: var(--pale-bar); color: var(--navy); font-size: 10px; }
  .web-bar__note { font-size: 6px; font-weight: 400; margin-right: 4px; }
  .web-bar__square { width: 7px; height: 7px; background: #3b5a9a; }

  .social-line {
    position: absolute; left: 490px; top: 198px; display: flex; align-items: center; gap: 6px;
    font-size: 12px; font-weight: 500; color: #fff;
  }
  .social-line__square { width: 22px; height: 22px; background: #3b5a9a; }

  .photo {
    position: absolute; border-radius: 50%; border: 4px solid #fff;
    box-shadow: 0 0 4px rgba(0,0,0,0.15);
  }
  .photo--large {
    left: 430px; top: 6px; width: 184px; height: 184px;
    background: radial-gradient(circle at 45% 55%, #e9c2a4 0%, #d9a483 40%, #eef2f6 78%);
  }
  .photo--small {
    left: 354px; top: 118px; width: 124px; height: 124px;
    background: radial-gradient(circle at 60% 45%, #e8c3a0 0%, #b39a85 45%, #6f7377 90%);
  }

  .sheet-footer {
    position: absolute; left: 93px; top: 1082px; width: 622px;
    display: flex; align-items: center; gap: 16px; font-family: "Arimo", Arial, sans-serif;
    color: var(--text-dark);
  }
  .sheet-footer__site { font-size: 11px; font-weight: 700; }
  .sheet-footer__rule { flex: 1; height: 1px; background: var(--rule); }
  .sheet-footer__version { font-size: 10.5px; }
</style>
</head>
<body>

<svg width="0" height="0" style="position:absolute">
  <defs>
    <linearGradient id="water-fill" x1="0" y1="0" x2="0" y2="1">
      <stop offset="0" stop-color="#b9cbe2"/>
      <stop offset="0.35" stop-color="#5f86b7"/>
      <stop offset="0.7" stop-color="#9bb4d3"/>
      <stop offset="1" stop-color="#d8e3f0"/>
    </linearGradient>
  </defs>
</svg>

<article class="banner banner--navy">
  <svg class="banner__water" viewBox="0 0 625 241" role="img" aria-label="Wasserwelle mit Luftblasen">
    <path d="M0 160 C80 190 170 200 260 185 C330 173 380 165 440 155 C520 140 580 120 625 95 L625 241 L0 241 Z" fill="url(#water-fill)"/>
  </svg>
  <div class="brand-mark"><span class="brand-mark__dot"></span><span class="brand-mark__name">www.kupferbogen.de</span></div>
  <h1 class="headline"><span class="headline__line">Ein schönes Bad…</span><span class="headline__line headline__line--second">…ist kein Zufall</span></h1>
  <p class="tagline">Badsanierung &amp; Neubau – Team Kupferbogen<span class="tagline__company">Bernd Kowalke GmbH</span></p>
  <div class="info-bar"><span class="info-bar__company">Bernd Kowalke GmbH</span><span>Lindenau | Mühlberg| Grabow | Tannrode (OT Eichfeld)</span></div>
  <div class="web-bar"><span class="web-bar__note">Weitere Infos unter</span><span class="web-bar__square"></span><span>kupferbogen.de</span></div>
  <div class="photo photo--large" role="img" aria-label="Foto: Frau am Waschtisch mit Armatur und fließendem Wasser"></div>
  <div class="photo photo--small" role="img" aria-label="Foto: Kind in der Badewanne unter der Handbrause"></div>
</article>

<article class="banner banner--pale">
  <svg class="banner__water" viewBox="0 0 625 241" role="img" aria-label="Wasserwelle mit Luftblasen">
    <path d="M0 160 C80 190 170 200 260 185 C330 173 380 165 440 155 C520 140 580 120 625 95 L625 241 L0 241 Z" fill="url(#water-fill)"/>
  </svg>
  <div class="brand-mark"><span class="brand-mark__dot"></span><span class="brand-mark__name">www.kupferbogen.de</span></div>
  <h1 class="headline"><span class="headline__line">Ein schönes Bad…</span><span class="headline__line headline__line--second">…ist kein Zufall</span></h1>
  <p class="tagline">Badsanierung &amp; Neubau – Team Kupferbogen<span class="tagline__company">Bernd Kowalke GmbH</span></p>
  <div class="info-bar"><span class="info-bar__company">Bernd Kowalke GmbH</span><span>Lindenau | Mühlberg| Grabow | Tannrode (OT Eichfeld)</span></div>
  <div class="web-bar"><span>www.kupferbogen.de</span></div>
  <div class="photo photo--large" role="img" aria-label="Foto: Frau am Waschtisch mit Armatur und fließendem Wasser"></div>
  <div class="photo photo--small" role="img" aria-label="Foto: Kind in der Badewanne unter der Handbrause"></div>
</article>

<article class="banner banner--bright">
  <svg class="banner__water" viewBox="0 0 625 241" role="img" aria-label="Wasserwelle mit Luftblasen">
    <path d="M0 160 C80 190 170 200 260 185 C330 173 380 165 440 155 C520 140 580 120 625 95 L625 241 L0 241 Z" fill="url(#water-fill)"/>
  </svg>
  <div class="brand-mark"><span class="brand-mark__dot"></span><span class="brand-mark__name">www.kupferbogen.de</span></div>
  <h1 class="headline"><span class="headline__line">Ein schönes Bad…</span><span class="headline__line headline__line--second">…ist kein Zufall</span></h1>
  <p class="tagline">Badsanierung &amp; Neubau – Team Kupferbogen<span class="tagline__company">Bernd Kowalke GmbH</span></p>
  <div class="info-bar"><span class="info-bar__company">Bernd Kowalke GmbH</span><span>Lindenau | Mühlberg| Grabow | Tannrode (OT Eichfeld)</span></div>
  <div class="social-line"><span class="social-line__square"></span><span>kupferbogen.de</span></div>
  <div class="photo photo--large" role="img" aria-label="Foto: Frau am Waschtisch mit Armatur und fließendem Wasser"></div>
  <div class="photo photo--small" role="img" aria-label="Foto: Kind in der Badewanne unter der Handbrause"></div>
</article>

<footer class="sheet-footer">
  <span class="sheet-footer__site">www.kupferbogen.de</span>
  <span class="sheet-footer__rule"></span>
  <span class="sheet-footer__version">Design 1_V2</span>
</footer>

</body>
</html>
```